Direct Mail Campaign for Safety Supply Company

Design a 6 inch x 11 inch direct mail piece targeting business contacts that purchase PPE (personal protection equipment) such as safety gloves, glasses, hard hats, vests, etc. <br/><br/>Target - Many different contacts in a business might be the buyer such as Safety Manager, Office Manager, Warehouse worker, etc. <br/><br/>Location - Will mail to business in Dallas close to their distribution warehouse at 2318 Marbury Ave Ste 40, Dallas, TX 75219<br/><br/>Competitive Advantages<br/>Speed - can deliver next day and in emergencies, potentially same day.<br/>Service - ability to speak directly to a person instead of being caught online<br/>Convenience - easy to work with<br/>Consultation - assistance with finding the right solutions for prospects company, increasing engagement and usage, employee satisfaction.

Target Market(s)

Contacts within a company that purchase personal protection equipment. It is a wide array of companies and contacts. Direct mail design should be either catchy or clever.

Industry/Entity Type

Safety

Font styles to use
Sans Serif

Colors

Designer to choose colors to be used in the design.

Requirements
Must have
• Front should have a great visual image with company logo and a short statement or tag line.
• Back should speak to reasons why they should try PWT. Leave 4" wide x 2" tall space for inkjetting on lower right.
Nice to have
• Open to ideas.

```html
<!DOCTYPE html>
<html lang="en">
<head>
<meta charset="utf-8">
<title>PWT Safety Supplies – Direct Mail</title>
<link href="https://fonts.googleapis.com/css2?family=Open+Sans:ital,wght@0,400;0,600;0,700;0,800;1,700;1,800&display=swap" rel="stylesheet">
<style>
  :root {
    --ink: #141414;
    --paper: #ffffff;
    --brand-dark: #1b1a1a;
    --alert-red: #e41b35;
    --safety-yellow: #e6c500;
    --tan-light: #e3d6c4;
    --tan-mid: #c5b197;
    --tan-deep: #8e7862;
    --placeholder: #eeeae3;
  }
  * { box-sizing: border-box; margin: 0; padding: 0; }
  html, body { width: 1200px; height: 2200px; overflow: hidden; background: var(--paper); }
  body { font-family: "Open Sans", Arial, sans-serif; color: var(--ink); }

  .mailer { position: relative; width: 1200px; height: 2200px; overflow: hidden; background: var(--paper); }

  .skyline {
    position: absolute; inset: 560px 0 0 0;
    background:
      linear-gradient(180deg, rgba(255,255,255,0) 0%, rgba(255,255,255,0) 55%, var(--tan-mid) 72%, var(--tan-deep) 100%),
      linear-gradient(90deg, rgba(255,255,255,0) 0%, rgba(255,255,255,0) 45%, var(--tan-light) 60%, var(--tan-mid) 100%);
  }

  .tagline {
    position: absolute; top: 52px; left: 0; width: 100%;
    text-align: center; font-size: 55px; font-weight: 600; letter-spacing: 0.5px;
  }

  .brand-name {
    position: absolute; top: 118px; left: 0; width: 100%;
    text-align: center; color: var(--brand-dark); font-weight: 800; line-height: 1;
  }
  .brand-name .brand-initials { display: block; font-size: 370px; letter-spacing: 20px; }
  .brand-name .brand-descriptor { display: block; font-size: 104px; margin-top: 10px; letter-spacing: 2px; }

  .product-card {
    position: absolute; width: 466px; height: 432px;
    border: 7px solid var(--safety-yellow); border-top: none;
    border-radius: 26px; background: var(--paper); overflow: hidden;
  }
  .product-card__title {
    height: 114px; background: var(--alert-red); color: var(--paper);
    font-size: 60px; font-weight: 600; text-align: center; line-height: 114px;
    margin: 0 -7px; letter-spacing: 1px;
  }
  .product-card__photo {
    margin: 30px 26px; height: 250px; border-radius: 10px; background: var(--placeholder);
  }
  .card-helmet { left: 64px; top: 688px; }
  .card-goggle { left: 64px; top: 1145px; }
  .card-gloves { left: 72px; top: 1602px; }
  .card-helmet .product-card__photo { background: radial-gradient(ellipse at 50% 55%, #f0dd2a 0%, #e8cf12 35%, #f4f1ea 70%); }
  .card-goggle .product-card__photo { background: radial-gradient(ellipse at 50% 55%, #55565a 0%, #7a7b7f 30%, #f1eee8 70%); }
  .card-gloves .product-card__photo { background: radial-gradient(ellipse at 50% 55%, #e8772a 0%, #e58a45 35%, #ece3d6 72%); }

  .advantages { position: absolute; left: 589px; top: 707px; width: 564px; }
  .advantages__banner {
    height: 87px; background: var(--safety-yellow); color: var(--ink);
    font-size: 33px; font-weight: 600; text-align: center; line-height: 87px; letter-spacing: 0.5px;
  }
  .advantage { position: absolute; left: 3px; width: 560px; }
  .advantage__name {
    color: var(--alert-red); font-size: 42px; font-weight: 800; font-style: italic; line-height: 1.05;
  }
  .advantage__text { font-size: 32px; font-weight: 600; line-height: 47px; }
  .adv-speed { top: 140px; }
  .adv-service { top: 434px; }
  .adv-convenience { top: 725px; }
  .adv-consultation { top: 938px; }

  .address {
    position: absolute; top: 2072px; left: 0; width: 100%;
    text-align: center; font-size: 55px; font-weight: 600; letter-spacing: 0.5px;
  }
</style>
</head>
<body>
<main class="mailer">
  <div class="skyline" role="img" aria-label="Faint tan silhouette of a construction site skyline with a tower crane, high-rise frames and heavy machinery"></div>

  <p class="tagline">Think Safe... Work Safe... Be Safe with...</p>

  <h1 class="brand-name">
    <span class="brand-initials">PWT</span>
    <span class="brand-descriptor">SAFETY SUPPLIES</span>
  </h1>

  <section class="product-card card-helmet">
    <h2 class="product-card__title">HELMET</h2>
    <div class="product-card__photo" role="img" aria-label="Yellow full-brim hard hat"></div>
  </section>

  <section class="product-card card-goggle">
    <h2 class="product-card__title">GOGGLE</h2>
    <div class="product-card__photo" role="img" aria-label="Smoke-tinted wraparound safety glasses"></div>
  </section>

  <section class="product-card card-gloves">
    <h2 class="product-card__title">GLOVES</h2>
    <div class="product-card__photo" role="img" aria-label="Orange cut-resistant work glove with black grip coating"></div>
  </section>

  <section class="advantages">
    <h2 class="advantages__banner">COMPETITIVE ADVANTAGES</h2>
    <div class="advantage adv-speed">
      <h3 class="advantage__name">SPEED</h3>
      <p class="advantage__text">can deliver next day and in emergencies, potentially same day.</p>
    </div>
    <div class="advantage adv-service">
      <h3 class="advantage__name">SERVICE</h3>
      <p class="advantage__text">ability to speak directly to a person instead of being caught online</p>
    </div>
    <div class="advantage adv-convenience">
      <h3 class="advantage__name">CONVENIENCE</h3>
      <p class="advantage__text">easy to work with</p>
    </div>
    <div class="advantage adv-consultation">
      <h3 class="advantage__name">CONSULTATION</h3>
      <p class="advantage__text">assistance with finding the right solutions for prospects company, increasing engagement and usage, employee satisfaction.</p>
    </div>
  </section>

  <p class="address">2318 Marbury Ave Ste 40, Dallas, TX 75219</p>
</main>
</body>
</html>
```